依頼概要
■ 依頼の目的/概要

弊社は「カード選びナビ広場 http://www.hoshizora-cardnavi.com/ 」というクレジットカードの比較サイトを運営しています。
今回はこのカード選びナビ広場のトップページのサイトデザインリニューアルをお願いします。

現在、サイト内( http://www.hoshizora-cardnavi.com/ )にある素材は自由に使って頂いて構いません。
既存のデザインを残しつつデザインをしていただいても
逆に完全新規にデザインをしていただいても構いません。
最終的なクオリティが高ければOKです。
素材サイトで何か素材を購入すればよりクオリティが高くなるのであれば
別途素材の購入も検討します。
その際はメッセージでご連絡ください。

■コーディング不要
コーディングは不要なので、デザインのみでOKです。

■ 希望するウェブデザイン

サイト訪問者が楽しくクレジットカードを選んだり
クレジットカードについての知識を学んだりできるようなデザインが希望です。
逆にサイト訪問者が堅苦しく感じてしまうようなデザインは避けたいです。
既存サイトでは下記URLのようなサイトデザインが好みです。

http://www.mz.tobira-net.com/mobile/index.html?bid=mz_gn_0007
http://www.mirumart.co.jp/kuruma/index.html?ca=top_glo_009
http://store.fenlow.com/jp/
http://store.tavix.jp/Special/Compare/Computer/Relmo/index.html

また「クレジットカード」で検索して1ページ目に出てくるサイトには
綺麗なサイトが多いので、こちらも参考にして頂きたいです。

【サイズの横幅について】

現在の横幅はぴったり950pxですが、
980px前後までであれば、横幅が大きくなっても構いません。
横幅が現在よりも小さくなるのは不可です。

ただし、ヘッダー部分とフッター部分は下記サイトのように横全体に広がっているデザインが希望です。
http://www.qrt.co.jp/ordercard/index.html

■ 納品ファイルの希望

第一希望 フォトショップ形式 + BMP形式
第二希望 イラストレーター形式 + BMP形式

■ 進め方

弊社の希望するイメージに近い提案を1つ(場合によって複数)選択させて頂きます。希望に近づけるために、修正要望を個別にさせて頂くこともあります。コンペ方式のため、修正後に当選されない場合も、どうかご了承ください。

■ その他/注意点

選択させて頂いたウェブデザインの著作権(財産権)等の扱いはTezukuri利用規約に従い、弊社に譲渡をお願いします。フォントや画像素材などを利用する場合は上記利用用途に使用できることを確認し、第三者の知的財産権等に注意して下さい。
■リニューアルによる変更点
今回のリニューアルではデザイン面だけでなくシステム面も強化するため
トップページのデザインが一部変更になります。
変更点は添付ファイルにまとめました。
なので現在のトップページのデザイン( http://www.hoshizora-cardnavi.com/
ではなく添付ファイル内のデザインを元にデザインをしてください。

```html
<!DOCTYPE html>
<html lang="ja">
<head>
<meta charset="utf-8">
<title>カード選びナビ広場</title>
<link href="https://fonts.googleapis.com/css2?family=Noto+Sans+JP:wght@400;700&display=swap" rel="stylesheet">
<style>
:root{
  --bg:#e8f0f6;
  --white:#ffffff;
  --blue:#2f7fc8;
  --blue-dark:#1f5e9c;
  --blue-light:#d9eaf8;
  --line:#c5d6e4;
  --text:#333a40;
  --muted:#6b7680;
  --orange:#f08a1c;
  --red:#d9352b;
  --yellow:#ffe79a;
  --card1:#c9d3db;
  --card2:#8fa7bd;
  --gold1:#d8bf72;
  --gold2:#a98832;
}
*{box-sizing:border-box;margin:0;padding:0}
html,body{width:1200px;height:3920px;overflow:hidden}
body{background:var(--bg);font-family:"Noto Sans JP",sans-serif;color:var(--text);font-size:13px;position:relative;line-height:1.5}
.abs{position:absolute}

/* header */
.site-header{left:0;top:0;width:1200px;height:170px;background:var(--white);border-bottom:1px solid var(--line)}
.site-header .strip{height:8px;background:var(--blue)}
.brand{left:44px;top:34px;display:flex;align-items:center;gap:12px}
.brand .mark{width:34px;height:34px;border-radius:50%;background:var(--orange)}
.brand .name{font-size:30px;font-weight:700;color:var(--blue-dark);white-space:nowrap}
.tagline{left:390px;top:46px;font-size:16px;font-weight:700;color:var(--blue-dark);white-space:nowrap}
.tagline em{font-style:normal;color:var(--red)}
.search{left:900px;top:30px;display:flex}
.search input{width:190px;height:30px;border:1px solid var(--line);border-radius:4px 0 0 4px;padding:0 8px;font-size:12px;font-family:inherit;color:var(--muted)}
.search button{width:60px;height:30px;border:0;background:var(--blue);color:#fff;border-radius:0 4px 4px 0;font-family:inherit;font-size:12px}
.util{left:900px;top:80px;font-size:11px;color:var(--muted)}

/* nav */
.global-nav{left:40px;top:180px;width:1120px;height:54px;display:flex;background:linear-gradient(#ffffff,#dfe9f2);border:1px solid var(--line);border-radius:6px}
.global-nav a{flex:1;display:flex;align-items:center;justify-content:center;font-size:14px;font-weight:700;color:var(--blue-dark);text-decoration:none;border-right:1px solid var(--line)}
.global-nav a:last-child{border-right:0}
.global-nav a:first-child{background:var(--blue);color:#fff;border-radius:6px 0 0 6px}

/* panels */
.panel{background:var(--white);border:1px solid var(--line);border-radius:6px;overflow:hidden}
.panel-head{height:44px;background:linear-gradient(var(--blue),var(--blue-dark));color:#fff;font-weight:700;font-size:15px;display:flex;align-items:center;padding-left:16px;gap:10px}
.panel-head .ico{width:22px;height:22px;background:#fff;border-radius:4px;opacity:.85}
.placeholder{border-radius:6px}
.card-img{width:150px;height:94px;border-radius:8px;background:linear-gradient(135deg,var(--card1),var(--card2))}
.card-img.gold{background:linear-gradient(135deg,var(--gold1),var(--gold2))}
.btn{display:inline-block;background:linear-gradient(#4e9ee0,var(--blue-dark));color:#fff;font-size:12px;font-weight:700;padding:5px 16px;border-radius:14px;text-decoration:none}
.btn.orange{background:linear-gradient(#f7a94a,#e07810)}

/* intro */
.intro{left:40px;top:256px;width:800px;height:244px;padding:18px}
.intro p{width:520px;font-size:13px;line-height:1.8}
.intro .mascot{position:absolute;right:30px;top:18px;width:200px;height:84px;background:linear-gradient(#e9f4fc,#bcdcf3)}
.news{position:absolute;left:18px;top:114px;width:764px;border:1px solid var(--line);border-radius:4px}
.news h3{font-size:12px;background:var(--blue-light);color:var(--blue-dark);padding:2px 10px}
.news li{list-style:none;font-size:12px;padding:2px 10px;display:flex;gap:16px;border-top:1px dotted var(--line);line-height:1.5}
.news .date{color:var(--muted)}
.news a{color:var(--blue-dark);text-decoration:underline}

/* popular */
.popular{left:40px;top:520px;width:800px;height:610px}
.pop-cols{display:flex;gap:10px;padding:14px}
.pop-col{flex:1;border:1px solid var(--line);border-radius:6px;text-align:center;padding-bottom:12px}
.pop-col .label{background:var(--yellow);padding:6px 0;font-weight:700;color:var(--red);font-size:17px;line-height:1.2}
.pop-col .label small{display:block;font-size:12px;color:var(--text)}
.pop-col .card-img{margin:12px auto 8px}
.pop-col .desc{font-size:11px;text-align:left;padding:0 10px;height:54px;color:var(--muted)}
.pop-row{display:flex;gap:10px;padding:0 14px}
.pop-box{flex:1;border:1px solid var(--line);border-radius:6px;padding:10px;display:flex;gap:8px;align-items:center}
.pop-box .card-img{width:100px;height:64px;flex:none}
.pop-box p{font-size:11px;color:var(--muted)}
.more{text-align:center;margin-top:14px}
.more span{display:inline-block;background:var(--blue-light);color:var(--blue-dark);font-weight:700;font-size:12px;padding:4px 24px;border-radius:12px}

/* features */
.features{left:40px;top:1150px;width:800px;height:376px}
.features h3{margin:12px 14px 8px;font-size:13px;color:var(--blue-dark);border-left:4px solid var(--orange);padding-left:8px}
.thumbs{display:grid;grid-template-columns:repeat(6,1fr);gap:12px 10px;padding:0 14px}
.thumb .pic{height:80px;border-radius:4px;background:linear-gradient(#dfe8ef,#9fb5c7)}
.thumb p{font-size:10px;color:var(--blue-dark);margin-top:4px;height:30px;line-height:1.4}

/* search */
.finder{left:40px;top:1546px;width:800px;height:1254px}
.finder .lead{font-size:12px;padding:12px 16px 4px;color:var(--muted)}
.group{margin:10px 16px 0;border:1px solid var(--line);border-radius:4px}
.group h4{background:var(--blue-light);color:var(--blue-dark);font-size:13px;padding:5px 10px;display:flex;gap:8px;align-items:center}
.group h4 span{font-weight:400;font-size:10px;color:var(--muted)}
.group h4::before{content:"";width:10px;height:10px;background:var(--blue);border-radius:2px}
.checks{display:grid;grid-template-columns:repeat(3,1fr);padding:6px 12px;gap:4px 10px}
.checks label{font-size:12px;display:flex;align-items:center;gap:6px;height:24px}
.checks i{width:14px;height:14px;border:1px solid #8fa3b3;background:#fff;border-radius:2px}
.select{margin:8px 12px;width:220px;height:28px;border:1px solid var(--line);border-radius:3px;font-size:12px;padding:4px 8px;color:var(--muted);display:flex;justify-content:space-between}
.result{margin:16px 16px 0;background:#fff6e0;border:1px solid #f0c878;border-radius:4px;text-align:center;padding:10px;font-size:14px;font-weight:700}
.result b{color:var(--red);font-size:22px}
.finder .go{text-align:center;margin-top:14px}
.finder .go .btn{font-size:15px;padding:10px 60px;border-radius:22px}
.finder .note{text-align:center;font-size:11px;color:var(--blue-dark);margin-top:12px}

/* battle */
.battle{left:40px;top:2830px;width:800px;height:980px}
.battles{display:grid;grid-template-columns:1fr 1fr;gap:16px;padding:16px}
.bout{border:1px solid var(--line);border-radius:6px;height:440px;overflow:hidden}
.bout h4{background:linear-gradient(#fff,var(--blue-light));font-size:14px;color:var(--blue-dark);text-align:center;padding:8px;border-bottom:1px solid var(--line)}
.bout .arena{display:flex;align-items:center;justify-content:center;gap:10px;height:300px;background:linear-gradient(#f4f8fb,#e3edf5)}
.bout .vs{font-size:26px;font-weight:700;color:var(--red)}
.bout .card-img{width:140px;height:88px}
.bout .names{display:flex;justify-content:space-around;font-size:11px;padding:10px 8px;color:var(--muted)}
.bout .acts{display:flex;justify-content:space-around}

/* sidebar */
.side{left:860px;width:300px}
.side-box{background:#fff;border:1px solid var(--line);border-radius:6px;overflow:hidden}
.side-box h3{background:linear-gradient(var(--blue),var(--blue-dark));color:#fff;font-size:13px;padding:8px 12px}
.rank li{list-style:none;display:flex;gap:8px;align-items:center;padding:8px 10px;border-bottom:1px dotted var(--line);font-size:12px}
.rank .no{width:22px;height:22px;border-radius:50%;background:var(--orange);color:#fff;font-weight:700;text-align:center;line-height:22px;font-size:12px;flex:none}
.rank .mini{width:56px;height:36px;border-radius:4px;background:linear-gradient(135deg,var(--card1),var(--card2));flex:none}
.banner{border:1px solid var(--line);border-radius:6px;background:#fff;padding:14px;text-align:center}
.banner .title{font-size:24px;font-weight:700;color:var(--blue-dark)}
.banner .sub{font-size:12px;color:var(--muted)}
.banner .hot{font-size:20px;font-weight:700;color:var(--red);margin:6px 0}
.banner .card-img{margin:8px auto}
.links li{list-style:none;font-size:12px;padding:6px 14px;border-bottom:1px dotted var(--line);color:var(--blue-dark)}
.links li::before{content:"▸ ";color:var(--orange)}

/* footer */
.site-footer{left:0;top:3830px;width:1200px;height:90px;background:var(--blue-light);border-top:3px solid var(--blue)}
.site-footer .fbrand{left:44px;top:18px;display:flex;gap:8px;align-items:center;font-weight:700;color:var(--blue-dark);font-size:18px}
.site-footer .fbrand .mark{width:22px;height:22px;border-radius:50%;background:var(--orange)}
.site-footer .fdesc{left:300px;top:14px;width:560px;font-size:10px;color:var(--muted)}
.site-footer .flinks{left:44px;top:56px;font-size:11px;color:var(--blue-dark)}
.site-footer .copy{left:700px;top:62px;font-size:10px;color:var(--muted)}
.site-footer .totop{left:1040px;top:18px;font-size:11px;background:#fff;border:1px solid var(--line);border-radius:4px;padding:4px 12px;color:var(--blue-dark)}
</style>
</head>
<body>

<header class="site-header abs">
  <div class="strip"></div>
  <div class="brand abs"><span class="mark"></span><span class="name">カード選びナビ広場</span></div>
  <div class="tagline abs">ライフスタイルに合った<em>お得な</em>クレジットカードを探そう!</div>
  <form class="search abs"><input value="キーワードを入力"><button type="button">検索</button></form>
  <div class="util abs">サイトマップ ｜ お問い合わせ ｜ 初めての方へ</div>
</header>

<nav class="global-nav abs">
  <a>カテゴリから探す</a><a>一覧から絞込み検索</a><a>一覧で比較</a><a>ブログ</a><a>クレジットカードを知る・特集</a>
</nav>

<section class="panel intro abs">
  <p>クレジットカードにはさまざまなサービスがあります。よくサービスを比較し、自分のライフスタイルに合ったクレジットカードを選ぶことでクレジットカードのメリットを最大限に活かすことができます。</p>
  <div class="mascot placeholder" role="img" aria-label="サイトのマスコットキャラクターのイラスト"></div>
  <div class="news">
    <h3>更新情報</h3>
    <ul>
      <li><span class="date">2012.05.16</span><a>人気のカード特集ページを公開しました</a></li>
      <li><span class="date">2012.05.10</span><a>旅行保険付きカードの比較表を更新しました</a></li>
      <li><span class="date">2012.04.28</span><a>ゴールドカード対決に新カードを追加しました</a></li>
      <li><span class="date">2012.04.20</span><a>ポイント還元率ランキングを更新しました</a></li>
    </ul>
  </div>
</section>

<section class="panel popular abs">
  <div class="panel-head"><span class="ico"></span>年会費別 当サイト人気クレジットカード</div>
  <div class="pop-cols">
    <div class="pop-col"><div class="label">年会費無料<small>部門</small></div><div class="card-img" role="img" aria-label="カード券面"></div><p class="desc">年会費ずっと無料で、ポイントも貯まる定番の一枚です。</p><span class="btn">詳しく見る</span></div>
    <div class="pop-col"><div class="label">1円～1,999円<small>部門</small></div><div class="card-img" role="img" aria-label="カード券面"></div><p class="desc">条件達成で年会費無料。初めての方にもおすすめ。</p><span class="btn">詳しく見る</span></div>
    <div class="pop-col"><div class="label">2,000円～9,999円<small>部門</small></div><div class="card-img" role="img" aria-label="カード券面"></div><p class="desc">旅行保険とポイントが充実した人気カードです。</p><span class="btn">詳しく見る</span></div>
    <div class="pop-col"><div class="label">10,000円以上<small>部門</small></div><div class="card-img gold" role="img" aria-label="ゴールドカード券面"></div><p class="desc">空港ラウンジなど上質な特典が揃うカードです。</p><span class="btn">詳しく見る</span></div>
  </div>
  <div class="pop-row">
    <div class="pop-box"><div class="card-img" role="img" aria-label="カード券面"></div><p>学生向けに特典が充実した年会費無料のカードです。</p></div>
    <div class="pop-box"><div class="card-img" role="img" aria-label="カード券面"></div><p>コンビニ利用でポイントが最大3倍になるカード。</p></div>
    <div class="pop-box"><div class="card-img" role="img" aria-label="カード券面"></div><p>電子マネー一体型で毎日の買い物がお得に。</p></div>
  </div>
  <div class="more"><span>もっと見る</span></div>
</section>

<section class="panel features abs">
  <div class="panel-head"><span class="ico"></span>クレジットカードを知る・特集</div>
  <h3>おすすめ記事をピックアップ</h3>
  <div class="thumbs">
    <div class="thumb"><div class="pic" role="img" aria-label="特集記事の写真"></div><p>旅行に強いカードの選び方</p></div>
    <div class="thumb"><div class="pic" role="img" aria-label="特集記事の写真"></div><p>初めてのカード入門</p></div>
    <div class="thumb"><div class="pic" role="img" aria-label="特集記事の写真"></div><p>ポイントを賢く貯めるコツ</p></div>
    <div class="thumb"><div class="pic" role="img" aria-label="特集記事の写真"></div><p>安全に使うための基礎知識</p></div>
    <div class="thumb"><div class="pic" role="img" aria-label="特集記事の写真"></div><p>セキュリティ対策まとめ</p></div>
    <div class="thumb"><div class="pic" role="img" aria-label="特集記事の写真"></div><p>年会費の仕組みを解説</p></div>
    <div class="thumb"><div class="pic" role="img" aria-label="特集記事の写真"></div><p>海外旅行保険の比較</p></div>
    <div class="thumb"><div class="pic" role="img" aria-label="特集記事の写真"></div><p>マイルが貯まるカード</p></div>
    <div class="thumb"><div class="pic" role="img" aria-label="特集記事の写真"></div><p>審査に通るためのポイント</p></div>
    <div class="thumb"><div class="pic" role="img" aria-label="特集記事の写真"></div><p>家族カードの活用術</p></div>
    <div class="thumb"><div class="pic" role="img" aria-label="特集記事の写真"></div><p>リボ払いの注意点</p></div>
    <div class="thumb"><div class="pic" role="img" aria-label="特集記事の写真"></div><p>ETCカードの作り方</p></div>
  </div>
</section>

<section class="panel finder abs">
  <div class="panel-head"><span class="ico"></span>クレジットカードを条件から絞り込んで探す</div>
  <p class="lead">ご希望の条件にチェックを入れると、該当するカードの枚数が表示されます。</p>
  <div class="group"><h4>サービス・特典<span>複数選択可</span></h4>
    <div class="checks">
      <label><i></i>ポイント還元率が高い</label><label><i></i>マイルが貯まる</label><label><i></i>ショッピング保険あり</label>
      <label><i></i>空港ラウンジ利用可</label><label><i></i>即日発行可能</label><label><i></i>学生でも申込み可</label>
      <label><i></i>ガソリン代割引</label><label><i></i>コンビニでお得</label><label><i></i>ネット通販でお得</label>
      <label><i></i>キャッシング可能</label><label><i></i>リボ払い専用</label><label><i></i>家族カードあり</label>
    </div></div>
  <div class="group"><h4>年会費<span>1つ選択</span></h4>
    <div class="checks">
      <label><i></i>年会費無料</label><label><i></i>初年度無料</label><label><i></i>条件付きで無料</label>
      <label><i></i>1円～1,999円</label><label><i></i>2,000円～9,999円</label><label><i></i>10,000円以上</label>
    </div></div>
  <div class="group"><h4>旅行保険<span>複数選択可</span></h4>
    <div class="checks">
      <label><i></i>海外旅行保険 自動付帯</label><label><i></i>海外旅行保険 利用付帯</label><label><i></i>国内旅行保険 自動付帯</label>
      <label><i></i>国内旅行保険 利用付帯</label><label><i></i>家族特約あり</label><label><i></i>航空機遅延保険あり</label>
    </div></div>
  <div class="group"><h4>種類<span>複数選択可</span></h4>
    <div class="checks">
      <label><i></i>一般カード</label><label><i></i>ゴールドカード</label><label><i></i>プラチナカード</label>
      <label><i></i>学生カード</label><label><i></i>女性向けカード</label><label><i></i>法人カード</label>
    </div></div>
  <div class="group"><h4>電子マネー<span>複数選択可</span></h4>
    <div class="checks">
      <label><i></i>ピコマネー</label><label><i></i>トレインパス</label><label><i></i>コンビニペイ</label>
      <label><i></i>モールペイ</label><label><i></i>タッチペイ</label><label><i></i>スピードペイ</label>
    </div></div>
  <div class="group"><h4>追加可能カード<span>複数選択可</span></h4>
    <div class="checks">
      <label><i></i>ETCカード</label><label><i></i>家族カード</label><label><i></i>電子マネーカード</label>
    </div></div>
  <div class="group"><h4>カードブランド</h4>
    <div class="select"><span>選択してください</span><span>▼</span></div></div>
  <div class="group"><h4>国際ブランド<span>複数選択可</span></h4>
    <div class="checks">
      <label><i></i>ハルカブランド</label><label><i></i>ソラノブランド</label><label><i></i>ニッポンカード</label>
      <label><i></i>ゴールドウェイ</label><label><i></i>ダイナス</label><label><i></i>こだわらない</label>
    </div></div>
  <div class="result">現在の条件で <b>67</b>枚 のカードが該当します</div>
  <div class="go"><span class="btn orange">この条件で検索する</span></div>
  <p class="note">▸ クレジットカードの一覧から絞り込む ｜ ▸ すべてのカードを比較する</p>
</section>

<section class="panel battle abs">
  <div class="panel-head"><span class="ico"></span>クレジットカード対決</div>
  <div class="battles">
    <div class="bout"><h4>スタンダードカード対決</h4>
      <div class="arena"><div class="card-img" role="img" aria-label="カード券面"></div><span class="vs">VS</span><div class="card-img" role="img" aria-label="カード券面"></div></div>
      <div class="names"><span>定番カードA</span><span>定番カードB</span></div>
      <div class="acts"><span class="btn">詳細を見る</span><span class="btn">詳細を見る</span></div></div>
    <div class="bout"><h4>コンビニでお得なクレジットカード対決</h4>
      <div class="arena"><div class="card-img" role="img" aria-label="カード券面"></div><span class="vs">VS</span><div class="card-img" role="img" aria-label="カード券面"></div></div>
      <div class="names"><span>コンビニカードA</span><span>コンビニカードB</span></div>
      <div class="acts"><span class="btn">詳細を見る</span><span class="btn">詳細を見る</span></div></div>
    <div class="bout"><h4>ゴールドカード対決</h4>
      <div class="arena"><div class="card-img gold" role="img" aria-label="ゴールドカード券面"></div><span class="vs">VS</span><div class="card-img gold" role="img" aria-label="ゴールドカード券面"></div></div>
      <div class="names"><span>ゴールドカードA</span><span>ゴールドカードB</span></div>
      <div class="acts"><span class="btn">詳細を見る</span><span class="btn">詳細を見る</span></div></div>
    <div class="bout"><h4>ポイント還元率でお得なカード対決</h4>
      <div class="arena"><div class="card-img" role="img" aria-label="カード券面"></div><span class="vs">VS</span><div class="card-img" role="img" aria-label="カード券面"></div></div>
      <div class="names"><span>ポイントカードA</span><span>ポイントカードB</span></div>
      <div class="acts"><span class="btn">詳細を見る</span><span class="btn">詳細を見る</span></div></div>
  </div>
</section>

<aside>
  <div class="side side-box abs" style="top:256px;height:440px">
    <h3>お得で人気のクレジットカード</h3>
    <ul class="rank">
      <li><span class="no">1</span><span class="mini"></span>あおば銀行 ルーキーカード</li>
      <li><span class="no">2</span><span class="mini"></span>ポイント還元カード</li>
      <li><span class="no">3</span><span class="mini"></span>トラベルプラスカード</li>
      <li><span class="no">4</span><span class="mini"></span>ショッピングカード</li>
      <li><span class="no">5</span><span class="mini"></span>プレミアゴールドカード</li>
      <li><span class="no">6</span><span class="mini"></span>学生応援カード</li>
    </ul>
  </div>
  <div class="side banner abs" style="top:716px;height:280px">
    <div class="sub">あおば銀行カード</div>
    <div class="title">ルーキーカード</div>
    <div class="hot">ポイント5倍</div>
    <div class="card-img" role="img" aria-label="カード券面"></div>
    <span class="btn orange">詳細はこちら</span>
  </div>
  <div class="side side-box abs" style="top:1016px;height:380px">
    <h3>カテゴリからカードを探す</h3>
    <ul class="links">
      <li>年会費無料カード</li><li>ポイント還元率が高いカード</li><li>マイルが貯まるカード</li><li>旅行保険付きカード</li>
      <li>ゴールドカード</li><li>学生向けカード</li><li>即日発行カード</li><li>電子マネー一体型カード</li><li>ETCカード</li>
    </ul>
  </div>
  <div class="side banner abs" style="top:1416px;height:240px">
    <div class="sub">あおば銀行カード</div>
    <div class="title">デイリーカード</div>
    <div class="hot">ポイント3倍</div>
    <span class="btn orange">詳細はこちら</span>
  </div>
  <div class="side side-box abs" style="top:1676px;height:520px">
    <h3>タイアップキャンペーン</h3>
    <ul class="links">
      <li>新規入会で最大5,000円分プレゼント</li><li>夏の旅行応援キャンペーン</li><li>ネット申込み限定特典</li>
      <li>家族カード同時申込み特典</li><li>ポイント2倍キャンペーン</li><li>学生限定キャッシュバック</li>
      <li>ゴールドカード初年度無料</li><li>ETCカード発行特典</li><li>電子マネーチャージ特典</li>
      <li>友達紹介キャンペーン</li><li>期間限定ポイント増量</li>
    </ul>
  </div>
  <div class="side banner abs" style="top:2216px;height:220px">
    <div class="title" style="font-size:20px">プレミアゴールドカード</div>
    <div class="card-img gold" role="img" aria-label="ゴールドカード券面"></div>
    <span class="btn">詳細はこちら</span>
  </div>
  <div class="side side-box abs" style="top:2456px;height:340px">
    <h3>クレジットカードの基礎知識</h3>
    <ul class="links">
      <li>クレジットカードの仕組み</li><li>支払い方法の種類</li><li>審査について</li><li>ポイントの貯め方</li>
      <li>付帯保険とは</li><li>国際ブランドの違い</li><li>よくある質問</li>
    </ul>
  </div>
</aside>

<footer class="site-footer abs">
  <div class="fbrand abs"><span class="mark"></span>カード選びナビ広場</div>
  <p class="fdesc abs">カード選びナビ広場は、さまざまなクレジットカードの特徴を比較し、あなたにぴったりの一枚を見つけるための情報サイトです。掲載情報は各社の公式情報をもとにしています。</p>
  <div class="flinks abs">ホーム ｜ 運営会社 ｜ お問い合わせ ｜ 免責事項 ｜ プライバシーポリシー ｜ サイトマップ</div>
  <div class="copy abs">Copyright © カード選びナビ広場 All Rights Reserved.</div>
  <div class="totop abs">▲ ページの先頭へ</div>
</footer>

</body>
</html>
```